Specialist aerospace company requires Powerpoint template

We are a company who delivers specialist engineering and testing services. We would like an updated Powerpoint template - specifically one that will be suitable to use in the production of training materials.
We would therefore like the following included:
-Our logo
-A copyright notice
-The course name (e.g. High Voltage Basics)
-The lesson name (e.g. Safe Clearances)
We wish to convey a professional image.

```html
<!DOCTYPE html>
<html lang="en">
<head>
<meta charset="utf-8">
<title>Stratovolt Training Template</title>
<link href="https://fonts.googleapis.com/css2?family=Ubuntu:wght@500;700&family=Lato:wght@400;700&display=swap" rel="stylesheet">
<style>
  :root{
    --page:#46525e;
    --slide:#ffffff;
    --ink:#2f3338;
    --title:#3a3f45;
    --blue:#3f6f9f;
    --blue-dark:#2f5a86;
    --muted:#5a6068;
    --ring:#c9d0d8;
    --photo-a:#5c6a78;
    --photo-b:#b9c3cc;
  }
  *{box-sizing:border-box;margin:0;padding:0}
  html,body{width:1200px;height:4147px;overflow:hidden;background:var(--page)}
  body{position:relative;font-family:'Lato',sans-serif;color:var(--ink)}
  .slide{position:absolute;left:43px;width:1112px;height:623px;background:var(--slide);overflow:hidden}
  .footer{position:absolute;left:0;bottom:0;width:100%;height:29px;background:var(--blue);color:#fff;font-size:12px;display:flex;justify-content:space-between;align-items:center;padding:0 30px 0 32px}
  .brand{position:absolute;display:flex;align-items:center;gap:10px;font-family:'Ubuntu',sans-serif;font-weight:500;color:var(--blue-dark)}
  .brand .mark{background:var(--blue-dark)}
  .brand-lg{left:29px;top:40px;font-size:34px}
  .brand-lg .mark{width:30px;height:30px}
  .brand-sm{right:28px;top:40px;font-size:21px}
  .brand-sm .mark{width:20px;height:20px}
  .slide-title{position:absolute;left:32px;top:20px;font-family:'Ubuntu',sans-serif;font-weight:500;font-size:56px;color:var(--title);letter-spacing:.5px}
  .slide-title span{color:var(--blue)}
  .body{font-size:18.5px;line-height:34px;color:var(--ink)}
  .lead{font-size:18.5px;line-height:34px;color:var(--blue);font-weight:700}
  .body p+p{margin-top:12px}
  .ticks{list-style:none;margin-top:20px}
  .ticks li{position:relative;padding-left:31px;font-size:17px;line-height:32px;color:var(--ink)}
  .ticks li svg{position:absolute;left:0;top:9px;width:15px;height:15px}
  .photo{position:absolute;background:linear-gradient(135deg,var(--photo-a),var(--photo-b))}
  .hero-svg{position:absolute;left:0;top:0}
  .hero-welcome{position:absolute;left:32px;top:200px;font-size:32px;font-weight:700;letter-spacing:.5px;color:var(--title)}
  .hero-name{position:absolute;left:30px;top:232px;font-size:72px;font-weight:700;letter-spacing:1px;color:var(--title)}
  .hero-intro{position:absolute;left:29px;top:340px;width:520px;font-size:19px;line-height:34px}
  .hero-date{position:absolute;left:29px;top:448px;display:flex;align-items:center;gap:14px;font-size:18.5px}
  .feature{position:absolute;top:233px;width:300px;text-align:center}
  .feature .icon{width:120px;height:120px;margin:0 auto;border-radius:50%;background:var(--ring);display:flex;align-items:center;justify-content:center}
  .feature .icon span{width:104px;height:104px;border-radius:50%;background:#4a5663;display:flex;align-items:center;justify-content:center}
  .feature .icon.blue span{background:var(--blue)}
  .feature h3{margin-top:20px;font-size:18px;font-weight:700;color:var(--ink)}
  .feature p{margin-top:10px;font-size:14.5px;line-height:26px;color:var(--ink)}
  .thanks{position:absolute;left:32px;top:185px;font-size:70px;font-weight:700;letter-spacing:1px;color:var(--title)}
  .contact{position:absolute;left:34px;display:flex;align-items:center;gap:22px;font-size:17px}
  .contact .ico{width:38px;height:38px;background:var(--blue);display:flex;align-items:center;justify-content:center}
</style>
</head>
<body>

<!-- Slide 1: Title -->
<section class="slide" style="top:55px">
  <div class="brand brand-lg"><i class="mark"></i>stratovolt</div>
  <div class="hero-welcome">WELCOME TO</div>
  <h1 class="hero-name">STRATOVOLT</h1>
  <p class="hero-intro">Lorem ipsum dolor sit amet, consectetur adipiscing eil, sed do eiusmod tempor incididunt ut labore et dolorem.</p>
  <div class="hero-date">
    <svg width="22" height="22" viewBox="0 0 22 22" fill="none" stroke="#3a3f45" stroke-width="1.6"><rect x="2" y="4" width="18" height="16" rx="1"/><path d="M2 9h18M7 2v4M15 2v4"/></svg>
    22 June 2023
  </div>
  <svg class="hero-svg" width="1112" height="595" viewBox="0 0 1112 595" role="img" aria-label="Engineer working on a 3D model of a mechanical assembly on a desktop monitor">
    <defs><linearGradient id="g1" x1="0" y1="0" x2="1" y2="1"><stop offset="0" stop-color="#c7ced5"/><stop offset=".5" stop-color="#6f7b87"/><stop offset="1" stop-color="#a9b2bb"/></linearGradient></defs>
    <circle cx="1200" cy="300" r="610" fill="none" stroke="var(--blue)" stroke-width="5" stroke-dasharray="1300 3000" stroke-dashoffset="-1260"/>
    <circle cx="1200" cy="300" r="586" fill="none" stroke="var(--blue)" stroke-width="16"/>
    <circle cx="1200" cy="300" r="560" fill="url(#g1)"/>
  </svg>
  <div class="footer"><span>©Copyrights 2023 Stratovolt. All Rights Reserved</span><span>01</span></div>
</section>

<!-- Slide 2: About -->
<section class="slide" style="top:735px">
  <h2 class="slide-title">About <span>Us</span></h2>
  <div class="brand brand-sm"><i class="mark"></i>stratovolt</div>
  <svg style="position:absolute;left:29px;top:127px" width="420" height="422" viewBox="0 0 420 422" role="img" aria-label="Smiling engineer in glasses working on a laptop in an office">
    <defs><linearGradient id="g2" x1="0" y1="0" x2="1" y2="1"><stop offset="0" stop-color="#3d4a55"/><stop offset=".6" stop-color="#7c8690"/><stop offset="1" stop-color="#c5cbd0"/></linearGradient></defs>
    <path d="M0 0H390L330 422H0Z" fill="url(#g2)"/>
    <path d="M300 10a60 60 0 0 1 70 70" fill="none" stroke="var(--blue)" stroke-width="12"/>
    <path d="M312 -2a72 72 0 0 1 80 90" fill="none" stroke="var(--blue)" stroke-width="4"/>
  </svg>
  <div style="position:absolute;left:501px;top:148px;width:580px">
    <p class="lead">Sed do eiusmod tempor incididunt ut labore et dolgna aliqua. Ut enim ad minim veniam, quis nostrud exercitationi ut aliquip ex ea commodo.</p>
    <div class="body" style="margin-top:18px">
      <p>Sed ut perspiciatis unde omnis iste natus error sit volm am doloremque laudantium, totam rem aperiam, eaque ipsa quae ab illo entore veritatis et quasi architecto beatae vitae dsunt explicabo. Nim ipsam voluptatem quia voluptas sit aspernatur aut odit aut fugit, sed quia consntur magni doloreui ratione voluptatem sequi nesciunt.</p>
      <p>Lorem ipsum dolor sit amet, consectetur adipiscing elit, sed do eiusmod tempor incididunt ut labore et dolgna aliqua. Ut enim ad minim veniam, quis nostrud exercitationi ut aliquip ex ea commodo consequat.</p>
    </div>
  </div>
  <div class="footer"><span>©Copyrights 2023 Stratovolt. All Rights Reserved</span><span>02</span></div>
</section>

<!-- Slide 3: Course -->
<section class="slide" style="top:1415px">
  <h2 class="slide-title">Course - <span>High Voltage Basics</span></h2>
  <div class="brand brand-sm"><i class="mark"></i>stratovolt</div>
  <div class="body" style="position:absolute;left:29px;top:157px;width:510px">
    <p>Sed ut perspiciatis unde omnis iste natus error sit doloremque laudantium, totam rem aperiam, eaque ipsa quae ab illo entore veritatis et quasi architecto beatae vitae dsunt explicabo. Nim ipsam voluptatem quia voluptas sit aut fugit, sed quia consntur magni doloreui ratione voluptatem sequi nesciunt.</p>
    <p>Eaque ipsa quae ab illo entore veritatis et quasi aitecto beatae vitae dsunt explicabo. Nim ipsam voluptatem quia voluptas sit aut fugit, sed quia consntur magni doloreui ratione voluptatem sequi nesciunt.</p>
  </div>
  <div style="position:absolute;left:575px;top:157px;width:520px">
    <p class="lead">Sed do eiusmod tempor incididunt ut labore et dolgna aliqua. Ut enim ad minim veniam, quis nostrud exercitioni.</p>
    <ul class="ticks">
      <li><svg viewBox="0 0 16 16"><circle cx="8" cy="8" r="6.5" fill="none" stroke="#3a3f45" stroke-width="1.6"/><path d="M5 8.2l2 2 4-4" fill="none" stroke="#3a3f45" stroke-width="1.6"/></svg>Lorem ipsum dolor sit amet, consectetur adipiscing elit, sed do eiusmod tempor incididunt ut labore et dolore magna aliqua.</li>
      <li><svg viewBox="0 0 16 16"><circle cx="8" cy="8" r="6.5" fill="none" stroke="#3a3f45" stroke-width="1.6"/><path d="M5 8.2l2 2 4-4" fill="none" stroke="#3a3f45" stroke-width="1.6"/></svg>Quis ipsum suspendisse ultrices gravidaisus commodo viverra maecenas accumsan lacus vel facilisis.</li>
      <li><svg viewBox="0 0 16 16"><circle cx="8" cy="8" r="6.5" fill="none" stroke="#3a3f45" stroke-width="1.6"/><path d="M5 8.2l2 2 4-4" fill="none" stroke="#3a3f45" stroke-width="1.6"/></svg>Lorem ipsum dolor sit amet, consectetur adipiscing elit, sed do eiusmod tempor incididunt ut labore et dolore magna aliqua.</li>
      <li><svg viewBox="0 0 16 16"><circle cx="8" cy="8" r="6.5" fill="none" stroke="#3a3f45" stroke-width="1.6"/><path d="M5 8.2l2 2 4-4" fill="none" stroke="#3a3f45" stroke-width="1.6"/></svg>Quis ipsum suspendisse ultrices gravidaisus commodo viverra maecenas accumsan lacus vel facilisis.</li>
    </ul>
  </div>
  <div class="footer"><span>©Copyrights 2023 Stratovolt. All Rights Reserved</span><span>03</span></div>
</section>

<!-- Slide 4: Lesson -->
<section class="slide" style="top:2095px">
  <h2 class="slide-title">Lesson - <span>Safe Clearances</span></h2>
  <div class="brand brand-sm"><i class="mark"></i>stratovolt</div>
  <div style="position:absolute;left:29px;top:157px;width:520px">
    <p class="lead">Sed do eiusmod tempor incididunt ut labore et dolgna aliqua. Ut enim ad minim veniam, quis nostrud exercitioni.</p>
    <ul class="ticks">
      <li><svg viewBox="0 0 16 16"><circle cx="8" cy="8" r="6.5" fill="none" stroke="#3a3f45" stroke-width="1.6"/><path d="M5 8.2l2 2 4-4" fill="none" stroke="#3a3f45" stroke-width="1.6"/></svg>Lorem ipsum dolor sit amet, consectetur adipiscing elit, sed do eiusmod tempor incididunt ut labore et dolore magna aliqua.</li>
      <li><svg viewBox="0 0 16 16"><circle cx="8" cy="8" r="6.5" fill="none" stroke="#3a3f45" stroke-width="1.6"/><path d="M5 8.2l2 2 4-4" fill="none" stroke="#3a3f45" stroke-width="1.6"/></svg>Quis ipsum suspendisse ultrices gravidaisus commodo viverra maecenas accumsan lacus vel facilisis.</li>
      <li><svg viewBox="0 0 16 16"><circle cx="8" cy="8" r="6.5" fill="none" stroke="#3a3f45" stroke-width="1.6"/><path d="M5 8.2l2 2 4-4" fill="none" stroke="#3a3f45" stroke-width="1.6"/></svg>Lorem ipsum dolor sit amet, consectetur adipiscing elit, sed do eiusmod tempor incididunt ut labore et dolore magna aliqua.</li>
      <li><svg viewBox="0 0 16 16"><circle cx="8" cy="8" r="6.5" fill="none" stroke="#3a3f45" stroke-width="1.6"/><path d="M5 8.2l2 2 4-4" fill="none" stroke="#3a3f45" stroke-width="1.6"/></svg>Quis ipsum suspendisse ultrices gravidaisus commodo viverra maecenas accumsan lacus vel facilisis.</li>
    </ul>
  </div>
  <div class="photo" role="img" aria-label="Smiling trainee holding a tablet in a training room" style="left:735px;top:130px;width:349px;height:400px;background:linear-gradient(160deg,#e6e9ec,#9aa3ad 60%,#6d7783)"></div>
  <div class="photo" role="img" aria-label="Team of engineers reviewing technical drawings at a table" style="left:578px;top:342px;width:324px;height:216px;border:3px solid #fff;background:linear-gradient(135deg,#c3ccd6,#5f7a96 55%,#aab6c2)"></div>
  <div class="footer"><span>©Copyrights 2023 Stratovolt. All Rights Reserved</span><span>04</span></div>
</section>

<!-- Slide 5: Why Choose Us -->
<section class="slide" style="top:2775px">
  <h2 class="slide-title">Why <span>Choose Us</span></h2>
  <div class="brand brand-sm"><i class="mark"></i>stratovolt</div>
  <p class="body" style="position:absolute;left:29px;top:108px;width:760px">Sed do eiusmod tempor incididunt ut labore et dolgna aliqua. Ut enim ad minim veniam, quis nostrud exercitioni.</p>

  <div class="feature" style="left:35px">
    <div class="icon"><span><svg width="52" height="52" viewBox="0 0 52 52" fill="none" stroke="#fff" stroke-width="2"><circle cx="20" cy="30" r="9"/><circle cx="20" cy="30" r="3.5"/><path d="M20 17v4M20 39v4M7 30h4M29 30h4M11 21l3 3M26 36l3 3M11 39l3-3M26 24l3-3"/><circle cx="36" cy="17" r="6"/><circle cx="36" cy="17" r="2"/><path d="M36 8v3M36 23v3M27 17h3M42 17h3"/></svg></span></div>
    <h3>LOREM IPSUM</h3>
    <p>Lorem ipsum dolor sit amet, consectetur adipi scing elit, sed do eiusmod tempor incididunt ut labore et dolore magna aliqua. Quis ipsum sus-pendisse ultrices gravida.</p>
  </div>
  <div class="feature" style="left:404px">
    <div class="icon blue"><span><svg width="52" height="52" viewBox="0 0 52 52" fill="none" stroke="#fff" stroke-width="2"><rect x="16" y="16" width="20" height="20" rx="2"/><rect x="22" y="22" width="8" height="8"/><path d="M21 16V8M26 16V6M31 16V8M21 36v8M26 36v10M31 36v8M16 21H8M16 26H6M16 31H8M36 21h8M36 26h10M36 31h8"/></svg></span></div>
    <h3>LOREM IPSUM</h3>
    <p>Lorem ipsum dolor sit amet, consectetur adipi scing elit, sed do eiusmod tempor incididunt ut labore et dolore magna aliqua. Quis ipsum sus-pendisse ultrices gravida.</p>
  </div>
  <div class="feature" style="left:773px">
    <div class="icon"><span><svg width="52" height="52" viewBox="0 0 52 52" fill="none" stroke="#fff" stroke-width="2"><rect x="6" y="9" width="40" height="32" rx="2"/><path d="M6 16h40"/><circle cx="24" cy="28" r="7"/><path d="M29 33l7 7"/></svg></span></div>
    <h3>LOREM IPSUM</h3>
    <p>Lorem ipsum dolor sit amet, consectetur adipi scing elit, sed do eiusmod tempor incididunt ut labore et dolore magna aliqua. Quis ipsum sus-pendisse ultrices gravida.</p>
  </div>
  <div class="footer"><span>©Copyrights 2023 Stratovolt. All Rights Reserved</span><span>05</span></div>
</section>

<!-- Slide 6: Thank you -->
<section class="slide" style="top:3455px">
  <div class="brand brand-lg"><i class="mark"></i>stratovolt</div>
  <h2 class="thanks">THANK YOU</h2>
  <div class="contact" style="top:312px">
    <span class="ico"><svg width="18" height="18" viewBox="0 0 24 24" fill="#fff"><path d="M6.6 10.8a15 15 0 0 0 6.6 6.6l2.2-2.2c.3-.3.7-.4 1-.2 1.1.4 2.3.6 3.6.6.6 0 1 .4 1 1V20c0 .6-.4 1-1 1A17 17 0 0 1 3 4c0-.6.4-1 1-1h3.5c.6 0 1 .4 1 1 0 1.3.2 2.5.6 3.6.1.3 0 .7-.2 1z"/></svg></span>
    CALL: +1 555-010-2040
  </div>
  <div class="contact" style="top:384px">
    <span class="ico"><svg width="16" height="20" viewBox="0 0 16 20" fill="#fff"><path d="M8 0a8 8 0 0 0-8 8c0 6 8 12 8 12s8-6 8-12a8 8 0 0 0-8-8zm0 11a3 3 0 1 1 0-6 3 3 0 0 1 0 6z"/></svg></span>
    Stratovolt, Address comes here
  </div>
  <div class="contact" style="top:456px">
    <span class="ico"><svg width="20" height="14" viewBox="0 0 20 14" fill="none" stroke="#fff" stroke-width="1.6"><rect x="1" y="1" width="18" height="12"/><path d="M1 1l9 7 9-7"/></svg></span>
    info@stratovolt-eng.com
  </div>
  <svg class="hero-svg" width="1112" height="595" viewBox="0 0 1112 595" role="img" aria-label="Engineer measuring a bearing with calipers over technical drawings">
    <defs><linearGradient id="g6" x1="0" y1="0" x2="1" y2="1"><stop offset="0" stop-color="#8c96a0"/><stop offset=".5" stop-color="#d9dee3"/><stop offset="1" stop-color="#a8b1ba"/></linearGradient></defs>
    <circle cx="1200" cy="300" r="610" fill="none" stroke="var(--blue)" stroke-width="5" stroke-dasharray="1300 3000" stroke-dashoffset="-1260"/>
    <circle cx="1200" cy="300" r="586" fill="none" stroke="var(--blue)" stroke-width="16"/>
    <circle cx="1200" cy="300" r="560" fill="url(#g6)"/>
  </svg>
  <div class="footer"><span>©Copyrights 2023 Stratovolt. All Rights Reserved</span><span>06</span></div>
</section>

</body>
</html>
```